Notepads for Marketing pieces-BOLD design

Looking for notepads for marketing pieces with logo, phone number, and website. Maybe something faded in background. Looking for bold and different

```html
<!DOCTYPE html>
<html lang="en">
<head>
<meta charset="utf-8">
<title>Zarvelicare Notepad</title>
<link rel="stylesheet" href="https://fonts.googleapis.com/css2?family=Poppins:wght@400;600;800&display=swap">
<style>
  :root {
    --brand-red: #e31b23;
    --ink: #111111;
    --rule: #cdb894;
    --paper: #ffffff;
    --backdrop: #e6e6e6;
    --faint-red: rgba(227, 27, 35, 0.07);
  }
  * { margin: 0; padding: 0; box-sizing: border-box; }
  html, body {
    width: 1154px;
    height: 1200px;
    overflow: hidden;
    background: var(--backdrop);
    font-family: "Poppins", sans-serif;
  }
  .notepad {
    position: absolute;
    left: 153px;
    top: 0;
    width: 848px;
    height: 1200px;
    background: var(--paper);
    overflow: hidden;
  }
  .brand-name {
    position: absolute;
    left: 64px;
    top: 92px;
    font-size: 44px;
    font-weight: 800;
    line-height: 1;
    letter-spacing: 1px;
    color: var(--brand-red);
    white-space: nowrap;
  }
  .brand-services {
    position: absolute;
    left: 64px;
    top: 150px;
    font-size: 13px;
    font-weight: 600;
    color: var(--ink);
    white-space: nowrap;
  }
  .contact {
    position: absolute;
    left: 571px;
    top: 79px;
    height: 50px;
    padding-left: 24px;
    border-left: 3px solid var(--brand-red);
    display: flex;
    flex-direction: column;
    justify-content: space-between;
    font-size: 15px;
    color: var(--ink);
  }
  .contact-item {
    display: flex;
    align-items: center;
    gap: 10px;
    line-height: 1;
    white-space: nowrap;
  }
  .contact-item svg { width: 15px; height: 15px; flex: none; }
  .backdrop-mark {
    position: absolute;
    left: 168px;
    top: 390px;
    width: 400px;
    height: 400px;
    border-radius: 50%;
    background: var(--faint-red);
  }
  .writing-lines {
    position: absolute;
    left: 45px;
    top: 197px;
    width: 757px;
  }
  .writing-lines span {
    display: block;
    height: 36px;
    border-top: 1.5px solid var(--rule);
  }
  .footer-band {
    position: absolute;
    left: 0;
    bottom: 0;
    width: 848px;
    height: 32px;
  }
</style>
</head>
<body>
  <main class="notepad">
    <div class="backdrop-mark" aria-hidden="true"></div>

    <header>
      <div class="brand-name">ZARVELICARE</div>
      <p class="brand-services">Home Health | Medical Staffing | Outpatien Therapy</p>

      <div class="contact">
        <div class="contact-item">
          <svg viewBox="0 0 16 16" aria-hidden="true">
            <path fill="#e31b23" d="M1 5c0-2 3-3 7-3s7 1 7 3v1.5h-3.5V5h-7v1.5H1z"/>
            <path fill="#e31b23" d="M4 7.5h8l2 6H2z"/>
            <circle cx="8" cy="10.5" r="1.6" fill="#fff"/>
          </svg>
          <span>555.014.0192</span>
        </div>
        <div class="contact-item">
          <svg viewBox="0 0 16 16" aria-hidden="true">
            <circle cx="8" cy="8" r="7" fill="#e31b23"/>
            <path fill="#fff" d="M5 4c2 0 3 1 2.5 2.5S5 7 5 9s-1.5 1-2 0 0-4 2-5zM10 8c1.5 0 2.5 1 2 2.5s-2 2.5-3 1.5 0-4 1-4z"/>
          </svg>
          <span>www.zarvelicare.org</span>
        </div>
      </div>
    </header>

    <section class="writing-lines" aria-label="Writing lines">
      <span></span><span></span><span></span><span></span><span></span>
      <span></span><span></span><span></span><span></span><span></span>
      <span></span><span></span><span></span><span></span><span></span>
      <span></span><span></span><span></span><span></span><span></span>
      <span></span><span></span><span></span><span></span><span></span>
    </section>

    <svg class="footer-band" viewBox="0 0 848 32" preserveAspectRatio="none" aria-hidden="true">
      <polygon points="0,0 657,0 630,32 0,32" fill="#e31b23"/>
      <polygon points="673,0 848,0 848,32 645,32" fill="#111111"/>
    </svg>
  </main>
</body>
</html>
```